TRV PowerPoint

I am looking for a clean, corporate PowerPoint template.

I would like the following:
- title slide
- break slide
- blank slide with title (for graphs or graphics)
- an ending slide.

Target Market(s)

Business professionals, medium to large business clients.

Requirements
Must have
• Must incorporate the TRV logo in either the header or footer

```html
<!DOCTYPE html>
<html lang="en">
<head>
<meta charset="utf-8">
<title>TRV Slide – Content Layout</title>
<link href="https://fonts.googleapis.com/css2?family=Source+Sans+3:wght@400;600;700&display=swap" rel="stylesheet">
<style>
  :root {
    --brand-blue: #0b4f9f;
    --heading-blue: #1a5aa8;
    --title-grey: #8a8a8a;
    --body-ink: #222222;
    --canvas-grey: #e8e8e8;
    --header-white: #ffffff;
    --panel-white: #ffffff;
    --rule-grey: #d6d6d6;
  }
  * { box-sizing: border-box; margin: 0; padding: 0; }
  html, body {
    width: 1200px;
    height: 875px;
    overflow: hidden;
    background: var(--canvas-grey);
    font-family: "Source Sans 3", "Myriad Pro", sans-serif;
  }
  .slide {
    position: relative;
    width: 1200px;
    height: 875px;
    background: var(--canvas-grey);
    overflow: hidden;
  }
  .slide-header {
    position: absolute;
    left: 0; top: 0;
    width: 100%;
    height: 80px;
    background: var(--header-white);
    border-bottom: 1px solid var(--rule-grey);
  }
  .page-title {
    position: absolute;
    left: 34px;
    top: 15px;
    font-size: 36px;
    font-weight: 400;
    color: var(--title-grey);
    letter-spacing: 0.2px;
  }
  .brand-name {
    position: absolute;
    right: 26px;
    top: 22px;
    font-size: 26px;
    font-weight: 600;
    color: var(--brand-blue);
    white-space: nowrap;
  }
  .content {
    position: absolute;
    left: 34px;
    top: 118px;
    width: 1112px;
  }
  .section-heading {
    font-size: 24px;
    font-weight: 400;
    color: var(--heading-blue);
    line-height: 1.2;
    margin-bottom: 8px;
  }
  .section-body {
    font-size: 15.6px;
    line-height: 27.5px;
    color: var(--body-ink);
    padding-left: 2px;
    margin-bottom: 26px;
  }
  .quote-panel {
    margin-left: -1.5px;
    width: 1122px;
    height: 142px;
    background: var(--panel-white);
    border-radius: 18px;
    padding: 16px 40px 0 32px;
    margin-top: 18px;
  }
  .quote-text {
    font-size: 15.6px;
    line-height: 27.5px;
    color: var(--body-ink);
  }
  .slide-footer {
    position: absolute;
    left: 0; bottom: 0;
    width: 100%;
    height: 23px;
    background: var(--brand-blue);
  }
  .version-label {
    position: absolute;
    right: 17px;
    top: 4px;
    font-size: 12.5px;
    font-weight: 700;
    color: #ffffff;
  }
</style>
</head>
<body>
<main class="slide">
  <header class="slide-header">
    <h1 class="page-title">Page heading goes here</h1>
    <div class="brand-name">TRV Tarn Ridge Ventures</div>
  </header>

  <section class="content">
    <h2 class="section-heading">Sub heading goes here</h2>
    <p class="section-body">Lorem ipsum dolor sit amet consecutor. Lorem ipsum dolor sit amet consecutor. Lorem ipsum dolor sit amet consecutor. Lorem ipsum dolor sit amet consecutor. Lorem ipsum dolor sit amet consecutor. Lorem ipsum dolor sit amet consecutor. Lorem ipsum dolor sit amet consecutor. Lorem ipsum dolor sit amet consecutor. Lorem ipsum dolor sit amet consecutor. Lorem ipsum dolor sit amet consecutor. Lorem ipsum dolor sit amet consecutor. Lorem ipsum dolor sit amet consecutor. Lorem ipsum dolor sit amet consecutor. Lorem ipsum dolor sit amet consecutor. Lorem ipsum dolor sit amet consecutor. Lorem ipsum dolor sit amet consecutor. Lorem ipsum dolor sit amet consecutor. Lorem ipsum dolor sit amet consecutor.</p>

    <h2 class="section-heading">Sub heading goes here</h2>
    <p class="section-body">Lorem ipsum dolor sit amet consecutor. Lorem ipsum dolor sit amet consecutor. Lorem ipsum dolor sit amet consecutor. Lorem ipsum dolor sit amet consecutor. Lorem ipsum dolor sit amet consecutor. Lorem ipsum dolor sit amet consecutor. Lorem ipsum dolor sit amet consecutor. Lorem ipsum dolor sit amet consecutor. Lorem ipsum dolor sit amet consecutor. Lorem ipsum dolor sit amet consecutor. Lorem ipsum dolor sit amet consecutor. Lorem ipsum dolor sit amet consecutor. Lorem ipsum dolor sit amet consecutor. Lorem ipsum dolor sit amet consecutor. Lorem ipsum dolor sit amet consecutor. Lorem ipsum dolor sit amet consecutor. Lorem ipsum dolor sit amet consecutor. Lorem ipsum dolor sit amet consecutor.</p>

    <h2 class="section-heading">Quotation goes here</h2>
    <blockquote class="quote-panel">
      <p class="quote-text">“Lorem ipsum dolor sit amet consecutor. Lorem ipsum dolor sit amet consecutor. Lorem ipsum dolor sit amet consecutor. Lorem ipsum dolor sit amet consecutor. Lorem ipsum dolor sit amet consecutor. Lorem ipsum dolor sit amet consecutor. Lorem ipsum dolor sit amet consecutor. Lorem ipsum dolor sit amet consecutor. Lorem ipsum dolor sit amet consecutor. Lorem ipsum dolor sit amet consecutor. Lorem ipsum dolor sit amet consecutor. Lorem ipsum dolor sit amet consecutor.”</p>
    </blockquote>
  </section>

  <footer class="slide-footer">
    <span class="version-label">version 1.0</span>
  </footer>
</main>
</body>
</html>
```